RW Talbrook LLC Business Card - Civil Engineering & Consulting Firm

We need a Business Card that is elegant, and masculine.  It is our Professional Civil Engineering & Consulting Company located in San Antonio TX (Not s construction or builder firm- no gears & no tool images please). We provide civil engineering services including  commercial site plans, grading and drainage plans, utility plans, hydraulics and hydrology, land planning, utility coordination, and other general civil engineering services related to commercial and residential development.
We have 2 existing Logos. We would like to convey reliability, strength, trustworthiness and attention to detail.  Blues and orange tones as per logo We are OK with the use of a darker blue in the mix.  We have 2 logo versions - Full Company Name Logo to go on the back of card, & Small Icon Logo for the front w/ personal Info.

Target Market(s)
Architects, Real Estate Developers, Other Strctural Engineers, Surveyers, General Contractors
Industry/Entity Type
Professional Civil Engineering
Contact Information for Business Card
Name, Position, Address, Cell & Office #, email, and company website
Font styles to use
Other font styles liked:
- Avian
Requirements
Should not have
- No Tools, No Gears, no Cranes, or Construction Equipment.

```html
<!DOCTYPE html>
<html lang="en">
<head>
<meta charset="utf-8">
<title>RW Talbrook LLC – Business Card</title>
<link rel="stylesheet" href="https://fonts.googleapis.com/css2?family=Poppins:wght@300;400;500;600&display=swap">
<style>
  :root {
    --stage: #d9d9d9;
    --paper: #ffffff;
    --blue: #6fa3d6;
    --orange: #ef8a1f;
    --yellow: #f6b21b;
    --ink: #5a5a5a;
  }
  * { box-sizing: border-box; margin: 0; padding: 0; }
  html, body { width: 1200px; height: 800px; overflow: hidden; }
  body {
    background: var(--stage);
    font-family: "Poppins", sans-serif;
    display: flex;
    align-items: center;
    justify-content: center;
    gap: 60px;
  }
  .card {
    position: relative;
    width: 520px;
    height: 297px;
    background: var(--paper);
    box-shadow: 0 10px 30px rgba(0,0,0,.15);
    overflow: hidden;
  }

  /* front */
  .accent-tick {
    position: absolute; top: 0; left: 170px;
    width: 5px; height: 18px; background: var(--yellow);
  }
  .brand-small {
    position: absolute; top: 70px; left: 34px;
    display: flex; align-items: center; gap: 8px;
    font-size: 13px; font-weight: 500; letter-spacing: 2px;
    color: var(--blue);
  }
  .brand-small .square { width: 12px; height: 12px; background: var(--orange); }
  .contact {
    position: absolute; top: 112px; left: 34px;
    font-size: 11.5px; line-height: 1.55; color: var(--ink);
    list-style: none;
  }
  .contact .label { color: var(--blue); }
  .address {
    position: absolute; top: 210px; left: 34px;
    font-size: 11.5px; line-height: 1.5; color: var(--ink);
    font-style: normal;
  }
  .name-bar {
    position: absolute; top: 0; right: 60px;
    width: 7px; height: 100%; background: var(--blue);
  }
  .identity {
    position: absolute; top: 50%; right: 74px;
    transform: translateY(-50%);
    writing-mode: vertical-rl;
    white-space: nowrap;
    text-align: center;
  }
  .identity .name {
    display: block; font-size: 18px; font-weight: 600;
    letter-spacing: 1px; color: var(--blue); line-height: 1.2;
  }
  .identity .role {
    display: block; font-size: 11.5px; color: var(--orange);
    letter-spacing: .5px; line-height: 1.3;
  }

  /* back */
  .card--back {
    display: flex; flex-direction: column; align-items: center; justify-content: center;
  }
  .wordmark {
    display: flex; align-items: center; gap: 12px;
    font-size: 40px; font-weight: 300; letter-spacing: 4px;
    color: var(--blue); line-height: 1;
  }
  .wordmark .square { width: 18px; height: 18px; background: var(--orange); }
  .tagline {
    margin-top: 8px; padding-top: 6px;
    border-top: 1.5px solid var(--blue);
    font-size: 10px; letter-spacing: 3px; color: var(--orange);
  }
  .website {
    margin-top: 26px;
    font-size: 10px; letter-spacing: 4px; color: var(--blue);
  }
</style>
</head>
<body>

  <section class="card card--front" aria-label="Business card front">
    <span class="accent-tick"></span>
    <div class="brand-small"><span class="square"></span>RW TALBROOK</div>
    <ul class="contact">
      <li><span class="label">Office:</span> 210 555 0148</li>
      <li><span class="label">Mobile:</span> 210 555 0149</li>
      <li><span class="label">Email:</span> daniel@talbrookeng.com</li>
      <li><span class="label">Web:</span> www.talbrookeng.com</li>
    </ul>
    <address class="address">118 Alamo Plaza<br>Suite 300, San Antonio<br>TX 78205</address>
    <span class="name-bar"></span>
    <div class="identity">
      <span class="name">DANIEL HARLOW</span>
      <span class="role">CEO/FOUNDER</span>
    </div>
  </section>

  <section class="card card--back" aria-label="Business card back">
    <div class="wordmark"><span class="square"></span>TALBROOK</div>
    <div class="tagline">LLC · CONSULTING ENGINEERS</div>
    <div class="website">WWW.TALBROOKENG.COM</div>
  </section>

</body>
</html>
```